Zia Bortolo's Crostoli

Looking for a packaging Label for Italian cookies. It has started with my great grandmothers Pizzelle recipe. Recipe has been in the family for over 100 years.
The packaging will be either clear plastic bags or Clear plastic hinged containers. Hoping for something elegant but traditional Italian. I have attached the company logo for color and idea possibilities
Would also like to give donation to helping animal foundations

Target Market(s)

Cookie lovers, coffee and tea drinkers, lighter alternative to heavy cookies

Requirements
Nice to have
• Family, Italian tradition

```html
<!DOCTYPE html>
<html lang="en">
<head>
<meta charset="utf-8">
<title>Zia Bortolo's Crostoli – Pizzelle Vanilla Label</title>
<link rel="stylesheet" href="https://fonts.googleapis.com/css2?family=Playfair+Display:wght@700;900&family=Playball&family=Roboto:wght@700&display=swap">
<style>
  :root {
    --backdrop: #c39a6d;
    --label-brown: #7f4b23;
    --rim-tan: #c9a27a;
    --rim-dark: #4a2a12;
    --shield-white: #ffffff;
    --accent-orange: #f7941d;
    --brand-orange: #e8601c;
    --flavour-blue: #26a8e0;
    --text-white: #ffffff;
    --flag-green: #009246;
    --flag-red: #ce2b37;
  }
  html, body {
    margin: 0;
    padding: 0;
    width: 1200px;
    height: 1200px;
    overflow: hidden;
    background: var(--backdrop);
  }
  .label-canvas {
    display: block;
    width: 1200px;
    height: 1200px;
  }
  .title-main {
    font-family: "Playfair Display", Georgia, serif;
    font-weight: 900;
    font-size: 100px;
    letter-spacing: 1px;
  }
  .title-script {
    font-family: "Playball", cursive;
    font-size: 56px;
    fill: var(--accent-orange);
  }
  .flavour-name {
    font-family: "Playfair Display", Georgia, serif;
    font-weight: 700;
    font-size: 48px;
    fill: var(--text-white);
  }
  .net-weight {
    font-family: "Roboto", Arial, sans-serif;
    font-weight: 700;
    font-size: 27px;
    fill: var(--text-white);
  }
  .brand-name {
    font-family: "Playfair Display", Georgia, serif;
    font-weight: 700;
    font-size: 40px;
    fill: var(--brand-orange);
  }
</style>
</head>
<body>
<svg class="label-canvas" viewBox="0 0 1200 1200" xmlns="http://www.w3.org/2000/svg">
  <defs>
    <clipPath id="label-disc">
      <circle cx="600" cy="621" r="348"/>
    </clipPath>
  </defs>

  <g class="label-disc">
    <circle cx="600" cy="621" r="360" fill="var(--label-brown)"/>
    <circle cx="600" cy="621" r="352" fill="none" stroke="var(--rim-tan)" stroke-width="5"/>
    <circle cx="600" cy="621" r="346" fill="none" stroke="var(--rim-dark)" stroke-width="4" stroke-dasharray="3 5"/>
    <circle cx="600" cy="621" r="341" fill="none" stroke="var(--rim-tan)" stroke-width="2"/>
  </g>

  <g class="flavour-band" clip-path="url(#label-disc)">
    <rect x="200" y="764" width="800" height="76" fill="var(--flavour-blue)"/>
  </g>

  <g class="brand-shield">
    <path d="M448 271 H750 V540 Q730 545 680 548 Q625 552 608 568 H592 Q575 552 520 548 Q470 545 448 540 Z" fill="var(--shield-white)"/>
    <text class="brand-name" x="599" y="405" text-anchor="middle">Zia</text>
    <text class="brand-name" x="599" y="455" text-anchor="middle">Bortolo's</text>
  </g>

  <circle class="handmade-badge" cx="363" cy="506" r="68" fill="none" stroke="var(--rim-tan)" stroke-width="2" opacity="0.7" role="img" aria-label="Handmade seal"/>

  <g class="italian-flag" role="img" aria-label="Italian flag">
    <rect x="792" y="327" width="25" height="105" fill="var(--flag-green)"/>
    <rect x="817" y="334" width="24" height="98" fill="var(--text-white)"/>
    <path d="M841 342 L865 360 V432 H841 Z" fill="var(--flag-red)"/>
  </g>

  <g class="product-title">
    <text class="title-main" x="604" y="684" text-anchor="middle" fill="var(--rim-tan)">PIZZELLE</text>
    <text class="title-main" x="600" y="680" text-anchor="middle" fill="var(--text-white)">PIZZELLE</text>
    <text class="title-script" x="600" y="728" text-anchor="middle">Italian waffle cookies</text>
  </g>

  <text class="flavour-name" x="600" y="818" text-anchor="middle">Vanilla</text>
  <text class="net-weight" x="600" y="889" text-anchor="middle">NET WT. 7oz (200g)</text>
</svg>
</body>
</html>
```